Private Learning Centre in Singapore needs a flyer design

We need a flyer design for our upcoming education fair and also able to use it for day to day purpose. The aim is to attract parents, students to enrol for classes by offering them free trial class/assessment. 2 sided flyer with the front page as the logo only and details on the other page. We would like to see a final design in blue, white and it should be curious and attractive enough not to allow customers to throw it away once they received it.

Education

```html
<!DOCTYPE html>
<html lang="en">
<head>
<meta charset="utf-8">
<title>Bright Grove Academy – Flyer</title>
<link href="https://fonts.googleapis.com/css2?family=Tinos:wght@400;700&display=swap" rel="stylesheet">
<style>
  :root {
    --brand-blue: #3b53a0;
    --brand-blue-soft: #5a70b4;
    --paper: #ffffff;
    --backdrop: #ece9e4;
    --photo-top: #4f7a5c;
    --photo-mid: #e7b9ae;
    --photo-low: #f3ece6;
  }
  * { margin: 0; padding: 0; box-sizing: border-box; }
  html, body { width: 1200px; height: 1000px; overflow: hidden; }
  body {
    background: var(--backdrop);
    font-family: "Tinos", "Times New Roman", serif;
    position: relative;
  }
  .flyer-front, .flyer-back {
    position: absolute;
    top: 35px;
    height: 940px;
    overflow: hidden;
    box-shadow: 0 2px 6px rgba(0,0,0,0.18);
  }
  .flyer-front { left: 143px; width: 450px; background: var(--brand-blue); }
  .flyer-back { left: 610px; width: 448px; background: var(--paper); }

  /* Front */
  .front-shapes { position: absolute; inset: 0; }
  .front-brand {
    position: absolute;
    left: 0; width: 450px; top: 190px;
    text-align: center;
    color: var(--brand-blue);
    font-weight: 400;
    font-size: 34px;
    letter-spacing: 3px;
    line-height: 1.25;
    text-transform: uppercase;
  }
  .front-offer {
    position: absolute;
    left: 0; width: 450px; top: 445px;
    text-align: center;
    color: var(--brand-blue);
    font-weight: 700;
    font-size: 74px;
    line-height: 84px;
  }
  .front-art {
    position: absolute;
    top: 735px;
    width: 175px; height: 205px;
    background: linear-gradient(180deg, rgba(255,255,255,0.18), rgba(255,255,255,0.42));
  }
  .front-art--left { left: 5px; }
  .front-art--right { left: 268px; }

  /* Back */
  .back-photo {
    position: absolute;
    left: 0; top: 0; width: 448px; height: 453px;
    background: linear-gradient(170deg, var(--photo-top) 0%, var(--photo-top) 22%, var(--photo-mid) 55%, var(--photo-low) 85%, #b77a4c 100%);
  }
  .back-intro {
    position: absolute;
    left: 22px; top: 490px; width: 404px;
    color: var(--brand-blue);
    font-size: 19.5px;
    line-height: 27px;
    text-align: justify;
  }
  .back-intro p + p { margin-top: 27px; }
  .back-subjects { text-align: left; padding-left: 6px; }
  .back-subjects span { margin-left: -6px; }

  .back-contact {
    position: absolute;
    left: 0; top: 770px; width: 448px; height: 170px;
    background: var(--brand-blue);
    color: var(--paper);
  }
  .contact-name {
    position: absolute;
    left: 34px; top: 13px;
    font-size: 21px;
  }
  .contact-rule {
    position: absolute;
    left: 22px; top: 43px; width: 286px; height: 1px;
    background: var(--paper);
  }
  .contact-list {
    position: absolute;
    left: 28px; top: 54px;
    list-style: none;
    font-size: 13.5px;
  }
  .contact-list li {
    display: flex; align-items: center;
    height: 23.5px;
  }
  .contact-icon { width: 14px; margin-right: 14px; display: flex; justify-content: center; }
  .social-square { width: 7px; height: 10px; background: var(--paper); }
  .contact-art {
    position: absolute;
    left: 294px; top: 10px; width: 148px; height: 155px;
    background: linear-gradient(180deg, rgba(255,255,255,0.18), rgba(255,255,255,0.42));
  }
</style>
</head>
<body>

<section class="flyer-front">
  <svg class="front-shapes" width="450" height="940" viewBox="0 0 450 940" aria-hidden="true">
    <circle cx="222" cy="223" r="178" fill="#ffffff"/>
    <circle cx="222" cy="540" r="193" fill="#ffffff"/>
  </svg>
  <div class="front-brand">Bright Grove<br>Academy</div>
  <div class="front-offer">FREE<br>TRIAL<br>CLASS</div>
  <div class="front-art front-art--left" role="img" aria-label="White silhouette of a leafy tree with a child reading beneath it"></div>
  <div class="front-art front-art--right" role="img" aria-label="White silhouette of a leafy tree with a child reading beneath it"></div>
</section>

<section class="flyer-back">
  <div class="back-photo" role="img" aria-label="Photo of a teacher and young pupils reading a book together in front of a chalkboard"></div>

  <div class="back-intro">
    <p>Bright Grove Academy is where you can de-velop academic and life skills.<br>
    Our teachers are the heartbeat of the business. They inspire and nurture students, helping them surpass their expectations.</p>
    <p class="back-subjects"><span>We cover:</span><br>English,&nbsp; Mathematics and Science<br>from Primary and Secondary Levels.</p>
  </div>

  <footer class="back-contact">
    <div class="contact-name">Bright Grove Academy</div>
    <div class="contact-rule"></div>
    <ul class="contact-list">
      <li>
        <span class="contact-icon">
          <svg width="9" height="12" viewBox="0 0 9 12"><path d="M4.5 0C2 0 0 2 0 4.4 0 7.6 4.5 12 4.5 12S9 7.6 9 4.4C9 2 7 0 4.5 0Zm0 6.2a1.8 1.8 0 1 1 0-3.6 1.8 1.8 0 0 1 0 3.6Z" fill="#fff"/></svg>
        </span>118 Marigold Lane S402215
      </li>
      <li>
        <span class="contact-icon">
          <svg width="8" height="13" viewBox="0 0 8 13"><rect x="0.75" y="0.75" width="6.5" height="11.5" rx="1.2" fill="none" stroke="#fff" stroke-width="1.5"/><rect x="3" y="10" width="2" height="1" fill="#fff"/></svg>
        </span>6271 5048
      </li>
      <li>
        <span class="contact-icon">
          <svg width="11" height="8" viewBox="0 0 11 8"><rect width="11" height="8" fill="#fff"/><path d="M0 0 5.5 4.5 11 0" fill="none" stroke="#3b53a0" stroke-width="1"/></svg>
        </span>hello@brightgroveacademy.com
      </li>
      <li>
        <span class="contact-icon"><span class="social-square"></span></span>/brightgroveacademy
      </li>
    </ul>
    <div class="contact-art" role="img" aria-label="White silhouette of a leafy tree with a child reading beneath it"></div>
  </footer>
</section>

</body>
</html>
```